IT COMPANYcutting edge tec business card

we are IT company that building any apps.
we need business card in japanese and english
You don’t have to include all information in front one you can attach part of that information to back-side
company name : 株式会社ひかりの丘 (BRIGHTHILL Inc.)
concept : cutting-edge technology
role : 取締役 (director)
name : 呉 炫秀 (Oh Hyeonsuk)
post number : 154-0038
address : 東京都世田谷区西若葉台5-14-8 (5-14-8, Nishiwakabadai, Setagaya Ku, Tokyo To, 154-0038, Japan)
Tel:+81-3-5917-2846
Mobile:+81-80-7253-3169
Email : hoh@brighthill-lab.com
website : www.brighthill-lab.com

we dont have logo so please make it as well
we also looking for designer who can make homapage design.

Contact Information for Business Card

cutting-edge design and modern for IT

Font styles to use
Sans Serif

Colors
34a6d7
33b8a4
6092c4
3377b5
886aae
6b449b
b868aa
a64599

Requirements
Must have
• Simple but designed

```html
<!DOCTYPE html>
<html lang="ja">
<head>
<meta charset="utf-8">
<title>BRIGHTHILL Inc. — Business Card</title>
<link rel="stylesheet" href="https://fonts.googleapis.com/css2?family=Lato:wght@300;400&family=Noto+Sans+JP:wght@300;400&display=swap">
<style>
  :root {
    --bg-light: #f1f1f1;
    --bg-dark: #cfcfcf;
    --card: #ffffff;
    --brand-blue: #34a6d7;
    --line-blue: #3377b5;
    --text-purple: #6b449b;
    --text-violet: #886aae;
    --avatar-start: #6092c4;
    --avatar-end: #886aae;
  }
  * { box-sizing: border-box; margin: 0; padding: 0; }
  html, body { width: 1200px; height: 900px; overflow: hidden; }
  body {
    background: radial-gradient(ellipse at 50% 40%, var(--bg-light) 0%, var(--bg-dark) 100%);
    font-family: "Lato", "Noto Sans JP", sans-serif;
    position: relative;
  }
  .card {
    position: absolute;
    top: 295px;
    width: 540px;
    height: 310px;
    background: var(--card);
    box-shadow: 0 12px 30px rgba(0,0,0,0.18), 0 2px 6px rgba(0,0,0,0.1);
  }
  .card--front { left: 40px; }
  .card--back { left: 620px; display: flex; align-items: center; justify-content: center; }

  .brand-name {
    font-family: "Lato", sans-serif;
    font-weight: 300;
    color: var(--brand-blue);
    letter-spacing: 0.04em;
    white-space: nowrap;
  }
  .card--front .brand-name {
    position: absolute;
    left: 0;
    width: 200px;
    top: 160px;
    text-align: center;
    font-size: 20px;
  }
  .card--back .brand-name { font-size: 44px; }

  .divider { position: absolute; left: 196px; top: 40px; }

  .contact {
    position: absolute;
    left: 228px;
    top: 42px;
    right: 20px;
    font-family: "Noto Sans JP", "Lato", sans-serif;
    font-weight: 400;
    font-size: 13px;
    line-height: 1.5;
    color: var(--text-purple);
  }
  .avatar {
    display: block;
    width: 36px;
    height: 36px;
    border-radius: 50%;
    background: linear-gradient(135deg, var(--avatar-start), var(--avatar-end));
    margin-bottom: 8px;
  }
  .contact .role, .contact .person { display: block; }
  .contact .email { color: var(--text-violet); margin-top: 14px; display: block; }
  .contact .web { color: var(--brand-blue); display: block; padding-left: 40px; }
</style>
</head>
<body>
  <section class="card card--front" aria-label="名刺 表面">
    <p class="brand-name">BRIGHTHILL Inc.</p>
    <svg class="divider" width="16" height="230" viewBox="0 0 16 230" aria-hidden="true">
      <path d="M14 2 H2 V228 H14" fill="none" stroke="var(--line-blue)" stroke-width="3"/>
    </svg>
    <div class="contact">
      <span class="avatar" role="img" aria-label="プロフィールアイコン"></span>
      <span class="role">取締役</span>
      <span class="person">呉 炫秀</span>
      <span class="line">Post number:154-0038</span><br>
      <span class="line">東京都世田谷区西若葉台5-14-8</span><br>
      <span class="line">Tel:+81-3-5917-2846</span><br>
      <span class="line">Mobile:+81-80-7253-3169</span>
      <span class="email">Email : hoh@brighthill-lab.com</span>
      <span class="web">www.brighthill-lab.com</span>
    </div>
  </section>

  <section class="card card--back" aria-label="名刺 裏面">
    <p class="brand-name">BRIGHTHILL Inc.</p>
  </section>
</body>
</html>
```